Business Card design for Property Developer

We need a business card design for a Melbourne based Property Developer called "Kestrelmoor Holdings Pty Ltd".

We subdivide land and onsell to builders etc.

We already have a company logo, which is attached. Also I have attached the layout requirements from the printer. We would like a 2-sided design with one side displaying our logo by itself and the other with the required info, such as name, address, tel no., email, abn etc. The card will need to be used by 4 members of staff so name and contact details should be interchangable.
Updates

If possible, can you please write "name' "job position" "phone" "email" "address" on the card but leave them so I can add the details at a later time. Thank you. Also I plan on printing with UV spot printing as a background on the card. Keep this is mind when designing.

Thanks again.

Hello designers, please do not include pics of houses, house plansĀ or construction machinery etc as we really do not like the way it looks. Thank you.

Target Market(s)

Real Estate Agents, Land Owners, Local Council Departments, Govt Bodies, other Developers etc.

Industry/Entity Type

Business

Requirements
Must have
• 2-sided design with one side displaying our logo by itself and the other with the required info, such as name, address, tel no., email, abn etc.

```html
<!DOCTYPE html>
<html lang="en">
<head>
<meta charset="utf-8">
<title>Kestrelmoor Holdings – Business Card</title>
<link rel="stylesheet" href="https://fonts.googleapis.com/css2?family=PT+Sans:wght@400;700&display=swap">
<style>
  :root {
    --backdrop: #e9e6e2;
    --card-white: #ffffff;
    --brand-red: #e31b23;
    --deep-red: #8f1519;
    --name-red: #9b1b1e;
    --brand-blue: #1f3f99;
    --ink: #2a2a2a;
    --white: #ffffff;
  }
  html, body {
    margin: 0;
    padding: 0;
    width: 1200px;
    height: 900px;
    overflow: hidden;
    background: var(--backdrop);
    font-family: "PT Sans", sans-serif;
  }
  .canvas {
    position: relative;
    width: 1200px;
    height: 900px;
  }
  .card {
    position: absolute;
    top: 297px;
    width: 488px;
    height: 306px;
    overflow: hidden;
    box-shadow: 0 2px 6px rgba(0,0,0,0.18);
  }
  /* Front: contact details */
  .card--details {
    left: 94px;
    background: var(--card-white);
  }
  .details-wordmark {
    position: absolute;
    left: 27px;
    top: 34px;
    margin: 0;
    font-size: 27px;
    font-weight: 700;
    letter-spacing: 0.5px;
    color: var(--brand-red);
    line-height: 1;
  }
  .person {
    position: absolute;
    left: 19px;
    top: 124px;
    color: var(--ink);
    font-size: 14.5px;
    line-height: 19px;
  }
  .person__name {
    margin: 0;
    font-size: 22px;
    font-weight: 700;
    color: var(--name-red);
    line-height: 24px;
  }
  .person__role { margin: 0 0 8px; }
  .person__company {
    margin: 0;
    font-weight: 700;
    color: var(--brand-blue);
  }
  .person__address { margin: 0 0 8px; font-style: normal; }
  .contact {
    list-style: none;
    margin: 0;
    padding: 0;
  }
  .contact li {
    display: flex;
    align-items: center;
    gap: 2px;
  }
  .contact svg { width: 16px; height: 12px; flex: none; }
  .details-band {
    position: absolute;
    left: 0;
    bottom: 0;
    width: 100%;
    height: 25px;
    background: linear-gradient(90deg, var(--deep-red) 0%, var(--brand-red) 45%, var(--brand-red) 80%, var(--deep-red) 100%);
  }
  /* Back: brand side */
  .card--brand {
    left: 620px;
    background: radial-gradient(ellipse 62% 78% at 50% 42%, #f0222a 0%, #d71a21 45%, var(--deep-red) 100%);
  }
  .brand-lockup {
    position: absolute;
    left: 0;
    right: 0;
    top: 78px;
    display: flex;
    flex-direction: column;
    align-items: center;
    gap: 22px;
  }
  .brand-lockup__dot {
    width: 96px;
    height: 96px;
    border-radius: 50%;
    background: var(--white);
  }
  .brand-lockup__name {
    margin: 0;
    font-size: 28px;
    font-weight: 700;
    letter-spacing: 0.5px;
    color: var(--white);
    line-height: 1;
  }
  .brand-web {
    position: absolute;
    left: 0;
    right: 0;
    top: 284px;
    margin: 0;
    text-align: center;
    font-size: 12px;
    letter-spacing: 2.4px;
    color: var(--white);
  }
</style>
</head>
<body>
<main class="canvas">
  <section class="card card--details" aria-label="Business card, contact side">
    <p class="details-wordmark">Kestrelmoor Holdings</p>
    <div class="person">
      <h1 class="person__name">Daniel Hartley</h1>
      <p class="person__role">Company Director</p>
      <p class="person__company">Kestrelmoor Holdings Pty Ltd</p>
      <address class="person__address">17 quarry lane, Ashgrove<br>County Tyrone BT71 4QP</address>
      <ul class="contact">
        <li>
          <svg viewBox="0 0 16 12" aria-hidden="true"><path d="M1 5 C1 2 4 1 8 1 C12 1 15 2 15 5 L12 6 L11 4 L5 4 L4 6 Z M4 6.5 L12 6.5 L13 11 L3 11 Z" fill="#9b1b1e"/></svg>
          <span>:0781-555-0143</span>
        </li>
        <li>
          <svg viewBox="0 0 16 12" aria-hidden="true"><rect x="1.5" y="1.5" width="13" height="9" fill="none" stroke="#9b1b1e" stroke-width="1.3"/><path d="M1.5 1.5 L8 7 L14.5 1.5 M1.5 10.5 L6 6 M14.5 10.5 L10 6" fill="none" stroke="#9b1b1e" stroke-width="1.1"/></svg>
          <span>:daniel@kestrelmoor.com</span>
        </li>
      </ul>
    </div>
    <div class="details-band"></div>
  </section>

  <section class="card card--brand" aria-label="Business card, brand side">
    <div class="brand-lockup">
      <div class="brand-lockup__dot"></div>
      <p class="brand-lockup__name">Kestrelmoor Holdings</p>
    </div>
    <p class="brand-web">www.kestrelmoor.com</p>
  </section>
</main>
</body>
</html>
```